Redesign of Grantlyhub.com

We need a redesign of some key-pages on our crowdfunding website for mobile apps, GrantlyHub.com.

- Redesign of homepage
http://www.grantlyhub.com/en

- Redesign of project submission page
http://www.grantlyhub.com/en/submit-your-app/submit-your-app

- Redesign of browsing section
http://www.grantlyhub.com/en/fund-apps

- Redesign of project funding page
http://www.grantlyhub.com/en/fund-apps/sponsor/sketch-riddler?amount=5.00

Design should be highly focused on a great user experience for users of the platform, being in principal mobile developers. So we need a great user experience for mobile developers using our service.

Benchmark designs we particularly like are:
http://www.pledgorama.com/
http://www.tradebitly.com/landing/
http://www.vomba.com/

Design should have a more 'fun, happy to get involved' factor as it has nox.
Updates

Logo's have been uploaded

Target Market(s)

mobile app developers

Industry/Entity Type

Crowdfunding

Requirements
Must have
• Submission forms must have explanation fields next to the form

Homepage should have design in whihc a introductary video can be integrated

```html
<!DOCTYPE html>
<html lang="en">
<head>
<meta charset="utf-8">
<title>GrantlyHub – Crowdfunding for Mobile Apps</title>
<link rel="stylesheet" href="https://fonts.googleapis.com/css2?family=Noto+Serif:wght@400;700&family=Arimo:wght@400;700&display=swap">
<style>
:root{
  --navy:#0d4f8b;
  --nav-blue:#4f8dc3;
  --gold:#f4c53a;
  --sky:#8fa8ee;
  --panel-border:#c9ced6;
  --ink:#222;
  --white:#fff;
}
*{box-sizing:border-box;margin:0;padding:0}
html,body{width:784px;height:1200px;overflow:hidden}
body{position:relative;background:#eef1f5;font-family:"Arimo",Arial,sans-serif;color:var(--ink)}
.abs{position:absolute}
.serif{font-family:"Noto Serif",Georgia,serif}

.site-header{left:0;top:0;width:784px;height:74px;background:var(--navy)}
.brand{left:66px;top:12px;display:flex;align-items:center;gap:8px;color:var(--white);font-size:19px}
.brand .mark{width:24px;height:24px;border:2px solid var(--white);border-radius:3px}
.top-links{right:226px;top:13px;font-size:8.5px;color:var(--white);font-family:"Noto Serif",Georgia,serif;white-space:nowrap;text-align:right}
.lang{left:575px;top:13px;font-size:8.5px;color:var(--white);font-family:"Noto Serif",Georgia,serif;white-space:nowrap}
.lang-select{left:625px;top:9px;width:100px;height:19px;background:var(--white);font-size:8.5px;padding:4px 6px;color:#333;font-family:"Noto Serif",Georgia,serif}
.lang-select::after{content:"";position:absolute;right:0;top:0;width:17px;height:19px;background:#5b7fa6}
.social{display:flex;gap:3px}
.social span{width:25px;height:25px;border-radius:5px;background:#3b67b0}
.social span+span{background:#37a6d8}
.header-social{left:502px;top:36px}
.search{left:573px;top:38px;width:152px;height:21px;background:var(--white);border-radius:2px;font-size:8.5px;color:#666;padding:5px 6px;font-family:"Noto Serif",Georgia,serif}

.page{left:54px;top:74px;width:676px;height:875px;background:var(--white)}
.main-nav{left:65px;top:86px;width:651px;height:33px;display:flex;background:var(--nav-blue);border:1px solid #2f6ba3}
.main-nav a{flex:auto;color:var(--white);text-decoration:none;font-family:"Noto Serif",Georgia,serif;font-size:11.5px;display:flex;align-items:center;justify-content:center;border-right:1px solid #2f6ba3;white-space:nowrap}
.main-nav a:last-child{border:0}
.main-nav a.active{background:var(--gold);flex:0 0 81px}

.hero{left:65px;top:126px;width:651px;height:229px;background:linear-gradient(135deg,#e9f1f8 0%,#fff 45%,#bcd9f0 70%,#2d86cf 100%)}
.hero-devices{left:165px;top:18px;width:320px;height:190px;background:linear-gradient(#3a3f46,#15181c);border-radius:10px}
.slide-arrow{width:18px;height:18px;top:226px}

.tabs{left:65px;top:369px;display:flex;gap:2px}
.tabs span{height:25px;width:146px;font-family:"Noto Serif",Georgia,serif;font-size:11.5px;display:flex;align-items:center;justify-content:center;background:linear-gradient(#e4e4e4,#bdbdbd);color:#333}
.tabs span.on{width:147px;background:linear-gradient(#c7e6f8,#7fc3ea)}
.tabs-rule{left:65px;top:398px;width:651px;height:3px;background:repeating-linear-gradient(90deg,#ccc 0 2px,transparent 2px 4px)}

.app-tile{width:72px;top:424px;text-align:center;font-size:8px;color:#333}
.app-tile .icon{width:72px;height:72px;border:1px solid #ccc;border-radius:5px;padding:4px;background:#fff;box-shadow:0 1px 2px #bbb}
.app-tile .icon div{width:100%;height:100%}
.app-tile p{margin-top:6px;white-space:nowrap}

.how-title{left:65px;top:532px;font-size:16px;font-weight:400}
.how-box{left:64px;top:557px;width:462px;height:175px;border:1px solid var(--panel-border);border-radius:3px}
.video{left:76px;top:569px;width:154px;height:154px;background:#000}
.how-text{left:245px;top:569px;width:270px;font-family:"Noto Serif",Georgia,serif;font-size:8.4px;line-height:11.8px;text-align:justify;color:#222}
.how-text p+p{margin-top:11px}

.fb-widget{left:535px;top:533px;width:180px;height:198px;border:1px solid #9fb3d8;background:#fff;font-size:7px}
.fb-head{left:7px;top:6px;display:flex;gap:6px}
.fb-head .sq{width:25px;height:25px;border:1px solid #9fb3d8;flex:none}
.fb-head b{color:#3b5998;font-size:9px;line-height:10px;display:block;width:140px}
.like-btn{left:40px;top:33px;width:31px;height:13px;border:1px solid #c0c6d2;background:#eef0f5;font-size:7px;padding:2px 4px;color:#3b5998}
.fb-count{left:7px;top:56px;width:168px;color:#333;line-height:9px}
.fans{left:7px;top:76px;display:grid;grid-template-columns:repeat(4,32px);column-gap:4px;row-gap:3px;text-align:center;color:#666;font-size:6px}
.fans i{display:block;width:32px;height:33px;margin-bottom:3px}
.fb-foot{left:5px;top:185px;font-size:6.5px;color:#777;display:flex;gap:4px;align-items:center}
.fb-foot span{width:8px;height:8px;background:#3b5998}

.band-head{top:750px;width:305px;height:34px;background:linear-gradient(#6a9fd0,#3f7bb3);border:1px solid #34689a;border-radius:3px 3px 0 0;color:var(--white);font-family:"Noto Serif",Georgia,serif;font-size:15px;padding:7px 15px}
.band-body{top:787px;width:305px;height:151px;border:1px solid #d5d8dd;background:linear-gradient(#fff,#e5e5e5);border-radius:2px}
.partner{font-family:"Noto Serif",Georgia,serif;font-weight:700;font-size:13px;color:#333;white-space:nowrap}
.badge{width:30px;height:30px;border-radius:50%;background:#2f6b3a}

.footer{left:0;top:949px;width:784px;height:223px;background:var(--sky)}
.ft-head{top:964px;font-family:"Noto Serif",Georgia,serif;font-size:15px;color:var(--white);font-weight:400}
.ft-links{top:998px;font-family:"Noto Serif",Georgia,serif;font-size:8.6px;color:var(--white);line-height:23.6px}
.ft-links li{list-style:none}
.ft-links li::before{content:"›";margin-right:6px}
.ft-divider{top:964px;width:1px;height:172px;background:#a9bcf2}
.ft-blog{left:252px;top:994px;width:190px;font-family:"Noto Serif",Georgia,serif;font-size:8.6px;line-height:11.8px;color:var(--white);text-align:justify}
.ft-blog p+p{margin-top:11px}
.field{left:486px;width:238px;background:var(--white);font-family:"Noto Serif",Georgia,serif;font-size:9px;font-weight:700;color:#333;padding:5px 6px}
.submit{left:485px;top:1085px;width:68px;height:22px;background:#4a7db0;border:1px solid #2e5f91;border-radius:3px;color:var(--white);font-family:"Noto Serif",Georgia,serif;font-size:11px;text-align:center;line-height:20px}
.footer-social{left:672px;top:1112px}
.copyright{left:54px;top:1182px;font-family:"Noto Serif",Georgia,serif;font-size:8.6px;color:#222}
</style>
</head>
<body>

<header class="abs site-header" aria-label="Site header"></header>
<div class="abs brand"><span class="mark"></span>GrantlyHub</div>
<div class="abs top-links">Blog&nbsp; | &nbsp;Get AAA Certified&nbsp; | &nbsp;login</div>
<div class="abs lang">Language</div>
<div class="abs lang-select">English</div>
<div class="abs social header-social" aria-label="Social links"><span></span><span></span></div>
<div class="abs search">Search</div>

<div class="abs page"></div>

<nav class="abs main-nav">
  <a class="active" href="#">Home</a>
  <a href="#">Fund Apps</a>
  <a href="#">Submit Your App</a>
  <a href="#">Find a Developer</a>
  <a href="#">How It Works</a>
  <a href="#">Register</a>
</nav>

<section class="abs hero" role="img" aria-label="Row of five smartphones showing app screens on a blue swirl background">
  <div class="abs hero-devices"></div>
</section>
<svg class="abs slide-arrow" style="left:74px" viewBox="0 0 18 18"><circle cx="9" cy="9" r="9" fill="#6f6f6f"/><path d="M10.5 5 6.5 9l4 4" stroke="#fff" stroke-width="2" fill="none"/></svg>
<svg class="abs slide-arrow" style="left:689px" viewBox="0 0 18 18"><circle cx="9" cy="9" r="9" fill="#9a9a9a"/><path d="M7.5 5l4 4-4 4" stroke="#fff" stroke-width="2" fill="none"/></svg>

<div class="abs tabs"><span class="on">Most Funded Apps</span><span>Our Staff's Picks</span><span>Successfully Funded</span></div>
<div class="abs tabs-rule"></div>

<div class="abs app-tile" style="left:72px"><div class="icon"><div role="img" aria-label="Chalkboard sketch game icon" style="background:linear-gradient(#2a2a2a 70%,#d98a2b 70%)"></div></div><p>Sketch Riddl...</p></div>
<div class="abs app-tile" style="left:166px"><div class="icon"><div role="img" aria-label="Colourful town game icon" style="background:linear-gradient(#7cc6ef,#d9a06b)"></div></div><p>Mila's New D...</p></div>
<div class="abs app-tile" style="left:259px"><div class="icon"><div role="img" aria-label="Pattern puzzle game icon" style="background:#c8141a"></div></div><p>PatternPebble</p></div>
<div class="abs app-tile" style="left:353px"><div class="icon"><div role="img" aria-label="Pixel warrior game icon" style="background:#2a3a1c"></div></div><p>Strata: Elde...</p></div>
<div class="abs app-tile" style="left:446px;top:422px"><div class="icon"><div role="img" aria-label="Chalkboard sketch game icon" style="background:linear-gradient(#2a2a2a 70%,#d98a2b 70%)"></div></div><p>Sketch Riddl...</p></div>
<div class="abs app-tile" style="left:540px;top:422px"><div class="icon"><div role="img" aria-label="Colourful town game icon" style="background:linear-gradient(#7cc6ef,#d9a06b)"></div></div><p>Mila's New D...</p></div>
<div class="abs app-tile" style="left:634px;top:421px"><div class="icon"><div role="img" aria-label="Pattern puzzle game icon" style="background:#c8141a"></div></div><p>PatternPebble</p></div>

<h2 class="abs how-title serif">How It Works</h2>
<div class="abs how-box"></div>
<div class="abs video" role="img" aria-label="Introductory video player">
  <svg width="154" height="154" viewBox="0 0 154 154"><path d="M71 56v44l29-22z" fill="#fff"/><rect x="8" y="142" width="138" height="2" fill="#888"/><rect x="11" y="138" width="2" height="10" fill="#fff"/></svg>
</div>
<div class="abs how-text">
  <p>Sed ut perspiciatis unde omnis iste natus error sit voluptatem accusantium doloremque laudantium, totam rem aperiam, eaque ipsa quae ab illo inventore veritatis et quasi architecto beatae vitae dicta sunt explicabo. Nemo enim ipsam voluptatem quia voluptas sit aspernatur aut odit aut fugit, sed quia consequuntur magni dolores eos qui ratione voluptatem sequi nesciunt.</p>
  <p>Neque porro quisquam est, qui dolorem ipsum quia dolor sit amet, consectetur, adipisci velit, sed quia non numquam eius modi tempora incidunt ut labore et dolore magnam aliquam</p>
  <p>quaerat voluptatem. Ut enim ad minima veniam, quis nostrum exetationem ullam corporis suscipit laboriosam, pariatur.</p>
</div>

<aside class="abs fb-widget">
  <div class="abs fb-head"><span class="sq"></span><b>GrantlyHub - Crowdfunding Mobile Apps <span style="font-weight:400;font-size:7px;color:#555">on Friendwall</span></b></div>
  <div class="abs like-btn">Like</div>
  <div class="abs fb-count">3,468 people like <b>GrantlyHub - Crowdfunding Mobile Apps</b>.</div>
  <div class="abs fans">
    <div><i role="img" aria-label="Fan photo" style="background:#6b5a4a"></i>Arjun</div>
    <div><i role="img" aria-label="Fan photo" style="background:#a4553b"></i>Paolo</div>
    <div><i role="img" aria-label="Fan photo" style="background:#d9cfc0"></i>Sena</div>
    <div><i role="img" aria-label="Fan photo" style="background:#8c7a66"></i>Subir</div>
    <div><i role="img" aria-label="Fan photo" style="background:#7a6a52"></i>Pierce</div>
    <div><i role="img" aria-label="Fan photo" style="background:#5a3528"></i>Kalina</div>
    <div><i role="img" aria-label="Fan photo" style="background:#3a3a3a"></i>Sanjay</div>
    <div><i role="img" aria-label="Fan photo" style="background:#c9d3e3"></i>Gurdeep</div>
  </div>
  <div class="abs fb-foot"><span></span>Friendwall social plugin</div>
</aside>

<div class="abs band-head" style="left:65px">Featured On</div>
<div class="abs band-body" style="left:65px">
  <span class="abs partner" style="left:60px;top:20px;font-size:10px">The Capitol Ledger</span>
  <span class="abs partner" style="left:175px;top:16px;font-size:15px">ByteWire</span>
  <span class="abs partner" style="left:60px;top:70px;font-size:17px">dataflux</span>
  <span class="abs partner" style="left:160px;top:72px;font-size:15px;font-weight:400">StartupIndex</span>
  <span class="abs partner" style="left:60px;top:124px;font-size:14px">FoundersPulse</span>
</div>

<div class="abs band-head" style="left:411px">Partners</div>
<div class="abs band-body" style="left:411px">
  <span class="abs partner" style="left:64px;top:12px;font-size:18px">velorix</span>
  <span class="abs partner" style="left:170px;top:10px;font-size:19px;font-weight:400">lumatek</span>
  <span class="abs partner" style="left:88px;top:68px;font-size:10px">Kinsei Corp</span>
  <span class="abs partner" style="left:180px;top:68px;font-size:8px">FJORD MOBILE</span>
  <span class="abs partner" style="left:64px;top:116px;font-size:16px;font-weight:400">Amber Lode</span>
  <span class="abs badge" style="left:190px;top:114px"></span>
</div>

<footer class="abs footer"></footer>
<h3 class="abs ft-head" style="left:54px">Quick Links</h3>
<ul class="abs ft-links" style="left:54px"><li>Home</li><li>About Us</li><li>Offers</li><li>Experience</li><li>Contact Us</li></ul>
<ul class="abs ft-links" style="left:147px"><li>Home</li><li>About Us</li><li>Offers</li><li>Experience</li><li>Contact Us</li></ul>
<div class="abs ft-divider" style="left:230px"></div>
<h3 class="abs ft-head" style="left:251px">Blog Posts</h3>
<div class="abs ft-blog">
  <p>Sed ut perspiciatis unde omnis iste natus error sit voluptatem accusantium doloremque laudantium, totam rem aperiam, eaque ipsa quae ab illo inventore veritatis et quasi architecto beatae vitae dicta sunt explicabo.</p>
  <p>Nemo enim ipsam voluptatem quia voluptas sit aspernatur aut odit aut fugit, sed quia consequuntur magni dolores eos qui ratione voluptatem sequi nesciunt.</p>
</div>
<div class="abs ft-divider" style="left:458px"></div>
<h3 class="abs ft-head" style="left:485px">Contact Us</h3>
<div class="abs field" style="top:997px;height:22px">Name</div>
<div class="abs field" style="top:1030px;height:42px">Message</div>
<div class="abs submit">Submit</div>
<div class="abs social footer-social" aria-label="Social links"><span></span><span></span></div>

<div class="abs copyright">Copyrights © 2012. All Rights Reserved.</div>

</body>
</html>
```